Plakat für Verein
Zielgruppe
Wir möchten eine Veranstaltung für unseren Verein - Hinterkalmbacher Heimatpflegeverein machen.
Aufgabenstellung
Die Party der Golden 20er
Glanz-Glamour-Lebenslust
Tanzen wie früher - Feiern wie nie
21. März - Uhrzeit: 20.30 im Saal KM
Live mit DJaneMarlies
Dresscode: Goldene 20er - Fransen, Federn, Hosenträger, Zylinder
Farbe: Gold/Schgwarz

```html
<!DOCTYPE html>
<html lang="de">
<head>
<meta charset="utf-8">
<title>Die Party der Golden 20er – Banner</title>
<link href="https://fonts.googleapis.com/css2?family=DM+Serif+Display&family=Playfair+Display:ital,wght@1,700&family=Libre+Caslon+Text:wght@700&display=swap" rel="stylesheet">
<style>
  :root{
    --page:#d6d6d6;
    --black:#0c0907;
    --brown-dark:#2a1d12;
    --brown:#5a3c1e;
    --gold-deep:#b98a35;
    --gold:#d9b560;
    --gold-light:#f7e3a0;
    --white:#ffffff;
    --sage:#7fa89c;
  }
  *{margin:0;padding:0;box-sizing:border-box}
  html,body{width:1200px;height:1117px;overflow:hidden;background:var(--page)}
  .banner{
    position:absolute;left:50px;top:337px;width:1100px;height:443px;overflow:hidden;
    background:
      radial-gradient(ellipse 55% 60% at 50% 40%, #4a3319 0%, transparent 70%),
      linear-gradient(180deg,var(--brown-dark) 0%, var(--black) 80%);
  }
  .banner__shapes{position:absolute;inset:0}
  .banner__text{position:absolute;left:0;width:100%;text-align:center;white-space:nowrap}
  .title{
    top:38px;font-family:"DM Serif Display",serif;font-size:90px;line-height:1;letter-spacing:-2px;
    background:linear-gradient(90deg,var(--gold-deep),var(--gold-light) 55%,var(--gold-deep));
    -webkit-background-clip:text;background-clip:text;color:transparent;
    filter:drop-shadow(4px 4px 0 rgba(0,0,0,.55));
  }
  .tagline{top:132px;font-family:"Playfair Display",serif;font-style:italic;font-weight:700;font-size:28px;color:var(--white);word-spacing:4px}
  .tagline .dot{color:var(--gold);font-size:20px;vertical-align:middle;margin:0 8px}
  .motto{top:191px;font-family:"DM Serif Display",serif;font-size:33px;letter-spacing:-1px;color:#1a1208}
  .date{top:238px;font-family:"DM Serif Display",serif;font-size:60px;letter-spacing:-1.5px;color:var(--white)}
  .live{top:296px;font-family:"DM Serif Display",serif;font-size:38px;color:var(--white)}
  .live .dj{color:var(--gold)}
  .footer{
    position:absolute;left:0;bottom:0;width:100%;height:72px;
    background:radial-gradient(ellipse 45% 120% at 50% 100%, #9a7a45 0%, var(--brown) 60%, #4a2f15 100%);
  }
  .footer__text{top:20px;font-family:"Libre Caslon Text",serif;font-weight:700;font-size:20px;letter-spacing:-.4px;color:var(--white)}
  .footer__text .sep{margin:0 14px;font-weight:400}
  .club-badge{
    position:absolute;left:953px;top:137px;width:126px;height:126px;border-radius:50%;
    background:var(--white);display:flex;align-items:center;justify-content:center;text-align:center;
    font-family:"Libre Caslon Text",serif;font-weight:700;font-size:11px;line-height:1.3;color:var(--sage);padding:14px;
  }
</style>
</head>
<body>
<div class="banner">
  <svg class="banner__shapes" width="1100" height="443" viewBox="0 0 1100 443">
    <defs>
      <linearGradient id="ribbonGold" x1="0" x2="1">
        <stop offset="0" stop-color="#b98a35"/><stop offset=".55" stop-color="#f7e3a0"/><stop offset="1" stop-color="#b98a35"/>
      </linearGradient>
    </defs>
    <g class="streaks" stroke="#e8b848" stroke-linecap="round">
      <line x1="0" y1="175" x2="115" y2="330" stroke-width="3" opacity=".8"/>
      <line x1="0" y1="215" x2="90" y2="340" stroke-width="1.5" opacity=".5"/>
      <line x1="60" y1="200" x2="230" y2="371" stroke-width="2" opacity=".7"/>
      <line x1="1020" y1="0" x2="1100" y2="95" stroke-width="4" opacity=".85"/>
      <line x1="990" y1="0" x2="1100" y2="135" stroke-width="2" opacity=".6"/>
      <line x1="900" y1="40" x2="1100" y2="300" stroke-width="1" opacity=".4"/>
      <line x1="1060" y1="0" x2="1100" y2="45" stroke-width="3" opacity=".9"/>
    </g>
    <g class="frame" stroke="#d9b560" stroke-width="2" fill="none">
      <polyline points="211,212 119,212 119,327 347,327"/>
      <polyline points="885,212 981,212 981,327 754,327"/>
    </g>
    <polygon class="ribbon" fill="url(#ribbonGold)" points="234,185 866,185 852,208 866,231 234,231 248,208"/>
  </svg>

  <div class="banner__text title">Die Party der Golden 20er</div>
  <div class="banner__text tagline">Glanz<span class="dot">●</span>Glamour<span class="dot">●</span>Lebenslust</div>
  <div class="banner__text motto">TANZEN WIE FRÜHER - FEIERN WIE NIE</div>
  <div class="banner__text date">21. März - Uhrzeit: 20.30 im Saal KM</div>
  <div class="banner__text live">Live mit <span class="dj">DJaneMarlies</span></div>

  <div class="club-badge">Hinterkalmbacher Heimatpflegeverein</div>

  <div class="footer">
    <div class="banner__text footer__text">Dresscode: Goldene 20er - Fransen, Federn, Hosenträger, Zylinder<span class="sep">|</span>Farbe: Gold/Schgwarz</div>
  </div>
</div>
</body>
</html>
```